FarBridge Webpage Look and feel re-design - Main page only

At FarBridge, we provide Video Streaming and Live Video Conferencing for the funeral industry. We currently have a fully functional website at www.farbridge-example.com, but we would like to change the look and feel to something simple, crisp and clean. A simple re-design of the .dwt file that can be applied to the entire site is all that is required. We are looking for ideas as to how to make it look clean, more technical and professional. We included a sample wireframe, BUT we are open to ideas of what YOU think would look good and professional! We also re-designed our logo for use on the site (uploaded) and simplified that. Bottom line, we need your artistic input - and the.dwt file modified to reflect this new look and feel. MUST be done in dreamweaver (have CC 2014) so modifications to the pages can be made on our end - no other formats please. Looking forward to your creativity! NOTE - winning designer will be given access to the site to make required modifications to the .dwt file...

Target Market(s)

Target Audience is Funeral Directors - we want the design simple and easy to navigate - most are between 30 - 65 North America based.

Industry/Entity Type

Industry

Font styles to use
Sans Serif

Requirements
Must have
• Must be somewhat easily navigable on a mobile device. Good contrast for wording, so it is easily read.
Nice to have
• Nice to have some original icons for our services such as in the wireframe...
Should not have
• Hard to read wording or clutter (such as our old site... Much too cluttered)

```html
<!DOCTYPE html>
<html lang="en">
<head>
<meta charset="utf-8">
<title>FarBridge – Video Casting Made Easy</title>
<link rel="stylesheet" href="https://fonts.googleapis.com/css2?family=Archivo+Black&family=Arimo:ital,wght@0,400;0,700;1,400&family=Open+Sans:wght@300;400&display=swap">
<style>
:root{
  --brand:#0b5a86;
  --brand-dark:#0a6388;
  --logo:#1f5c91;
  --text:#666;
  --muted:#8a8a8a;
  --light-band:#ececec;
  --footer:#3e3e3e;
  --footer-bottom:#343434;
  --footer-text:#bdbdbd;
  --white:#fff;
  --tick:#8cc63f;
}
*{margin:0;padding:0;box-sizing:border-box}
html,body{width:1006px;height:1200px;overflow:hidden;background:var(--white)}
body{position:relative;font-family:"Arimo",Arial,sans-serif;color:var(--text)}

/* header */
.header{position:absolute;left:0;top:0;width:1006px;height:65px;background:var(--white);border-bottom:1px solid #ddd}
.logo{position:absolute;left:144px;top:16px;display:flex;align-items:center;gap:6px}
.logo-dot{width:30px;height:30px;border-radius:50%;background:#c9cdd2}
.logo-name{font-weight:700;font-size:15px;color:var(--logo)}
.nav{position:absolute;left:286px;top:0;height:64px;display:flex}
.nav-item{height:64px;border-left:1px solid #e3e3e3;display:flex;align-items:center;justify-content:center;font-size:11px;color:#777;padding-top:4px}
.nav-item:last-child{border-right:1px solid #e3e3e3}
.caret{display:inline-block;margin-left:6px;border-left:3px solid transparent;border-right:3px solid transparent;border-top:3px solid #888;vertical-align:middle}
.login{position:absolute;left:647px;top:22px;width:79px;height:22px;background:var(--brand-dark);color:var(--white);font-size:9.5px;display:flex;align-items:center;justify-content:center;gap:5px}
.social{position:absolute;top:20px;width:23px;height:23px;border-radius:50%;background:#d0d0d0}

/* dropdown */
.dropdown{position:absolute;left:284px;top:65px;width:144px;background:var(--white);border:1px solid #ccc;z-index:2}
.dropdown a{display:block;height:29px;line-height:29px;padding-left:12px;font-size:9.5px;color:var(--brand);text-decoration:none;border-top:1px solid #555}
.dropdown a:first-child{border-top:none}

/* hero */
.hero{position:absolute;left:0;top:65px;width:1006px;height:400px;background:radial-gradient(ellipse at 72% 55%,#3a2c24 0%,#1a1512 35%,#070707 70%)}
.hero-title{position:absolute;left:132px;top:98px;font-family:"Archivo Black",sans-serif;font-size:20.5px;font-weight:400;color:var(--white);letter-spacing:.3px}
.hero-sub{position:absolute;left:132px;top:136px;font-family:"Open Sans",sans-serif;font-weight:300;font-size:19px;color:var(--white)}
.play-box{position:absolute;left:132px;top:181px;width:49px;height:49px;border-radius:5px;background:linear-gradient(#f2f2f2,#cfcfcf)}
.watch{position:absolute;left:193px;top:188px;font-family:"Archivo Black",sans-serif;font-size:14px;color:var(--white)}
.watch-sub{position:absolute;left:193px;top:208px;font-family:"Open Sans",sans-serif;font-weight:300;font-size:16px;color:var(--white)}
.checks{position:absolute;left:138px;top:250px;list-style:none}
.checks li{height:28px;display:flex;align-items:center;gap:8px;font-family:"Open Sans",sans-serif;font-weight:300;font-size:12.5px;color:var(--white)}
.arrow{position:absolute;top:180px}

/* testimonial */
.quote-band{position:absolute;left:0;top:465px;width:1006px;height:129px;background:var(--light-band)}
.quote-mark{position:absolute;font-family:Georgia,serif;font-size:26px;color:#b8b8b8}
.quote-text{position:absolute;left:170px;top:35px;width:600px;font-style:italic;font-size:13px;line-height:21.5px;color:var(--muted)}
.quote-author{position:absolute;left:171px;top:87px;font-size:10.5px;color:var(--brand)}

/* features */
.section-title{position:absolute;left:0;top:638px;width:1006px;text-align:center;font-size:19px;font-weight:400;color:var(--brand);letter-spacing:.2px}
.feature{position:absolute;top:695px;width:220px;text-align:center}
.feature-icon{height:92px;display:flex;align-items:center;justify-content:center}
.feature h3{font-weight:400;font-size:13.5px;color:var(--brand);margin-top:12px;line-height:18px}
.feature p{font-size:10px;line-height:18px;color:var(--muted);margin-top:7px}

/* call to action */
.cta{position:absolute;left:0;top:903px;width:1006px;height:87px;background:var(--brand-dark)}
.cta-text{position:absolute;left:144px;top:35px;font-size:13.5px;color:var(--white)}
.cta-btn{position:absolute;left:638px;top:23px;width:217px;height:40px;border-radius:3px;background:linear-gradient(#fafafa,#dde2e6);color:var(--brand);font-size:12px;display:flex;align-items:center;justify-content:center}

/* footer */
.footer{position:absolute;left:0;top:990px;width:1006px;height:165px;background:var(--footer)}
.footer-col{position:absolute;top:36px;width:150px}
.footer-col h4{font-weight:400;font-size:13px;color:var(--white);padding-bottom:9px;border-bottom:1px solid #5a5a5a}
.footer-col ul{list-style:none;margin-top:6px}
.footer-col li{font-size:9px;line-height:19px;color:var(--footer-text);padding-left:1px}
.footer-logo{position:absolute;left:712px;top:34px;display:flex;align-items:center;gap:8px}
.footer-logo .dot{width:70px;height:70px;border-radius:50%;background:#5a5a5a}
.footer-logo .name{font-weight:700;font-size:18px;color:#777}
.footer-bottom{position:absolute;left:0;top:1155px;width:1006px;height:45px;background:var(--footer-bottom);text-align:center;font-size:8.5px;line-height:45px;color:var(--footer-text)}
</style>
</head>
<body>

<header class="header">
  <div class="logo"><span class="logo-dot"></span><span class="logo-name">FarBridge</span></div>
  <nav class="nav">
    <div class="nav-item" style="width:82px">Services<span class="caret"></span></div>
    <div class="nav-item" style="width:93px">Community<span class="caret"></span></div>
    <div class="nav-item" style="width:85px">Company<span class="caret"></span></div>
    <div class="nav-item" style="width:75px">Contact</div>
  </nav>
  <div class="login">
    <svg width="9" height="9" viewBox="0 0 10 10"><circle cx="5" cy="3" r="2.5" fill="#fff"/><path d="M0 10c0-3 2-4.5 5-4.5S10 7 10 10z" fill="#fff"/></svg>
    LOGIN &raquo;
  </div>
  <span class="social" style="left:742px"></span>
  <span class="social" style="left:773px"></span>
  <span class="social" style="left:806px"></span>
  <span class="social" style="left:839px"></span>
</header>

<div class="dropdown">
  <a href="#">&raquo;&nbsp; Open Stream</a>
  <a href="#">&raquo;&nbsp; Open Presence</a>
  <a href="#">&raquo;&nbsp; Open Mobile</a>
</div>

<section class="hero" role="img" aria-label="Photo of a cameraman filming through a professional video camera on a dark background">
  <h1 class="hero-title">VIDEO CASTING MADE EASY!</h1>
  <p class="hero-sub">Just One Button - Simply press to start and stop</p>
  <div class="play-box">
    <svg width="49" height="49" viewBox="0 0 49 49"><circle cx="24.5" cy="24.5" r="14" fill="#bbb"/><circle cx="24.5" cy="24.5" r="11" fill="#e9e9e9"/><path d="M20 17l11 7.5L20 32z" fill="#d32020"/></svg>
  </div>
  <p class="watch">WATCH A SHORT VIDEO</p>
  <p class="watch-sub">to see how it works</p>
  <ul class="checks">
    <li><svg width="13" height="11" viewBox="0 0 13 11"><path d="M1 6l4 4 7-9" fill="none" stroke="var(--tick)" stroke-width="2.2"/></svg>No Computer Needed</li>
    <li><svg width="13" height="11" viewBox="0 0 13 11"><path d="M1 6l4 4 7-9" fill="none" stroke="var(--tick)" stroke-width="2.2"/></svg>Client’s Love it</li>
    <li><svg width="13" height="11" viewBox="0 0 13 11"><path d="M1 6l4 4 7-9" fill="none" stroke="var(--tick)" stroke-width="2.2"/></svg>New Revenue</li>
  </ul>
  <svg class="arrow" style="left:63px" width="14" height="56" viewBox="0 0 14 56"><path d="M13 1L1 28l12 27" fill="none" stroke="#555" stroke-width="1"/></svg>
  <svg class="arrow" style="left:932px" width="14" height="56" viewBox="0 0 14 56"><path d="M1 1l12 27L1 55" fill="none" stroke="#555" stroke-width="1"/></svg>
</section>

<section class="quote-band">
  <span class="quote-mark" style="left:143px;top:18px">&ldquo;</span>
  <p class="quote-text">This is new exciting technology being brought to us by FarBridge and it is taking our profession into a new realm of service.</p>
  <span class="quote-mark" style="left:768px;top:52px">&rdquo;</span>
  <p class="quote-author">Martin Keller, General Manager, Birchwood Funeral Homes Limited, Ontario, Canada</p>
</section>

<h2 class="section-title">THE VIDEO CASTING PLATFORM YOU WILL LOVE</h2>

<div class="feature" style="left:169px">
  <div class="feature-icon">
    <svg width="100" height="72" viewBox="0 0 100 72">
      <rect x="2" y="14" width="66" height="56" rx="8" fill="var(--brand)"/>
      <rect x="14" y="2" width="24" height="14" rx="4" fill="var(--brand)"/>
      <rect x="42" y="2" width="24" height="14" rx="4" fill="var(--brand)"/>
      <rect x="12" y="33" width="40" height="6" fill="#fff"/>
      <path d="M72 42l26-20v48z" fill="var(--brand)"/>
    </svg>
  </div>
  <h3>Open Stream</h3>
  <p>Full feature video casting for<br>funerals made easy</p>
</div>

<div class="feature" style="left:387px">
  <div class="feature-icon">
    <svg width="94" height="90" viewBox="0 0 100 92">
      <path d="M38 4l12 12 12-12" fill="none" stroke="var(--brand)" stroke-width="4"/>
      <rect x="5" y="18" width="90" height="68" rx="10" fill="var(--brand)"/>
      <rect x="12" y="25" width="62" height="50" rx="6" fill="#fff"/>
      <rect x="16" y="29" width="54" height="42" rx="4" fill="var(--brand)"/>
      <path d="M38 42l13 8-13 8z" fill="#fff"/>
      <circle cx="84" cy="52" r="3" fill="#fff"/><circle cx="84" cy="62" r="3" fill="#fff"/>
    </svg>
  </div>
  <h3>Open Presence</h3>
  <p>Participate in the ceremony even<br>if you cannot be there</p>
</div>

<div class="feature" style="left:609px">
  <div class="feature-icon">
    <svg width="72" height="90" viewBox="0 0 80 92">
      <path d="M18 58a30 30 0 1 1 44 0" fill="none" stroke="var(--brand)" stroke-width="7" stroke-linecap="round"/>
      <path d="M28 48a17 17 0 1 1 24 0" fill="none" stroke="var(--brand)" stroke-width="6" stroke-linecap="round"/>
      <circle cx="40" cy="35" r="8" fill="var(--brand)"/>
      <path d="M33 46h14l-4 40h-6z" fill="var(--brand)"/>
    </svg>
  </div>
  <h3>Open Mobile</h3>
  <p>Video cast from anywhere with<br>a SlateTab or PocketFone</p>
</div>

<section class="cta">
  <p class="cta-text">Let us provide you with an analysis of the revenue potential for your business.</p>
  <div class="cta-btn">Click here to contact us today</div>
</section>

<footer class="footer">
  <div class="footer-col" style="left:144px">
    <h4>Company</h4>
    <ul><li>Our Story</li><li>Press</li><li>Privacy Policy</li></ul>
  </div>
  <div class="footer-col" style="left:338px">
    <h4>Services</h4>
    <ul><li>Open Stream</li><li>Open Presence</li><li>Open Mobile</li></ul>
  </div>
  <div class="footer-col" style="left:532px">
    <h4>Services</h4>
    <ul><li>Testimonials</li><li>Partners</li><li>Help</li></ul>
  </div>
  <div class="footer-logo"><span class="dot"></span><span class="name">FarBridge</span></div>
</footer>
<div class="footer-bottom">©2014. FarBridge. All rights reserved.</div>

</body>
</html>
```